Flyer Design Print Ad for Clothing Store

We are a modest women's clothing store. We are looking for a print ad 90*134 mm that is attention grabbing and can serve as a template for us going forward. We cannot use pictures of actual women. We need it to include our logo, store hours, physical address, website, phone number. We would use this template and change the call to action as necessary e. g. BOGO Sale, 30% off, flash sale, summer sale etc. Our colors are black and white and our fonts are Bodoni sans and Athens.

Target Market(s)

Women from teen to age 70

Industry/Entity Type

Women's clothing

Font styles to use
Other font styles liked:
• Athens, Bodoni Sans

Requirements
Must have
• Our, logo, phone number, website, address and store hours
Nice to have
• I'd like something that's not just our flat logo but something that will make someone pause to look
Should not have
• Pictures of women

```html
<!DOCTYPE html>
<html lang="en">
<head>
<meta charset="utf-8">
<title>Orvelle – BOGO Sale Print Ad</title>
<link href="https://fonts.googleapis.com/css2?family=Marcellus&family=Open+Sans:wght@400;600;700&display=swap" rel="stylesheet">
<style>
  :root {
    --stage: #0e151a;
    --paper: #e4d9cc;
    --paper-light: #ece4da;
    --paper-dark: #d3c3b1;
    --ink: #0f1820;
    --band-black: #0d1317;
    --band-grey: #2a2f33;
    --white: #ffffff;
    --stroke-cream: #f1ebe1;
  }
  * { box-sizing: border-box; margin: 0; padding: 0; }
  html, body {
    width: 720px; height: 1200px; overflow: hidden;
    background: var(--stage);
  }
  .canvas { position: relative; width: 720px; height: 1200px; }
  .ad {
    position: absolute; left: 10px; top: 79px;
    width: 700px; height: 1042px; overflow: hidden;
    background: radial-gradient(ellipse at 50% 35%, var(--paper-light) 0%, var(--paper) 55%, var(--paper-dark) 100%);
    color: var(--ink);
    font-family: "Open Sans", Arial, sans-serif;
  }
  .ad > * { position: absolute; }
  .backdrop-ornament {
    left: 40px; top: 20px; width: 620px; height: 720px;
    border-radius: 50%;
    background: radial-gradient(circle, rgba(255,255,255,0.28) 0%, rgba(255,255,255,0.08) 60%, rgba(255,255,255,0) 75%);
  }
  .brush-stroke {
    left: 0; top: 390px; width: 660px; height: 190px;
    border-radius: 50% 40% 40% 50% / 60% 50% 50% 40%;
    background: linear-gradient(100deg, rgba(241,235,225,0.9) 0%, rgba(241,235,225,0.55) 55%, rgba(241,235,225,0) 100%);
    transform: rotate(-6deg);
  }
  .pattern-disc {
    left: -190px; top: 620px; width: 350px; height: 350px;
    border-radius: 50%;
    background: radial-gradient(circle at 65% 50%, #cbbcaa 0%, #bfae9a 100%);
    opacity: 0.8;
  }
  .brand-name {
    left: 0; right: 0; top: 218px; text-align: center;
    font-family: "Open Sans", Arial, sans-serif;
    font-size: 36px; font-weight: 600; letter-spacing: 1px; color: var(--ink);
  }
  .headline {
    left: 0; right: 0; top: 332px; text-align: center;
    font-family: "Marcellus", Georgia, serif;
    font-size: 92px; line-height: 1; font-weight: 400; color: var(--ink);
    text-shadow: 0 0 6px rgba(255,255,255,0.8);
  }
  .offer {
    left: 0; right: 0; top: 458px; text-align: center;
    font-family: "Marcellus", Georgia, serif;
    font-size: 84px; line-height: 1; color: var(--ink);
    text-shadow: 0 0 6px rgba(255,255,255,0.8);
  }
  .offer-sup { font-size: 44px; vertical-align: 34px; margin-left: 2px; }
  .details { left: 0; right: 0; top: 636px; text-align: center; }
  .details p { line-height: 1.2; }
  .hours { font-size: 23px; font-weight: 700; margin-bottom: 10px; }
  .hebrew-address { font-size: 32px; margin-top: 14px; }
  .english-address { font-size: 26px; font-weight: 700; margin-top: 6px; }
  .landmark { font-size: 19px; margin-top: 6px; }
  .directions { font-size: 17px; font-weight: 700; margin-top: 6px; }
  .buses { font-size: 17px; font-weight: 700; margin-top: 6px; }
  .band-phone {
    left: 0; top: 930px; width: 700px; height: 62px;
    background: var(--band-black); color: var(--white);
    text-align: center; font-size: 48px; font-weight: 600;
    letter-spacing: 5px; line-height: 62px;
  }
  .band-web {
    left: 0; top: 992px; width: 700px; height: 50px;
    background: var(--band-grey); color: var(--white);
    text-align: center; font-family: "Marcellus", Georgia, serif;
    font-size: 28px; letter-spacing: 4px; line-height: 50px;
  }
</style>
</head>
<body>
<div class="canvas">
  <section class="ad">
    <div class="backdrop-ornament" role="img" aria-label="Large faint floral ornament over a damask pattern on textured paper"></div>
    <div class="brush-stroke" role="img" aria-label="Cream paint brush stroke behind the headline"></div>
    <div class="pattern-disc" role="img" aria-label="Circle filled with a small damask pattern"></div>

    <div class="brand-name">Orvelle</div>
    <h1 class="headline">BOGO SALE</h1>
    <div class="offer">30%<span class="offer-sup">OFF</span></div>

    <div class="details">
      <p class="hours"><span dir="ltr">S-Th - 10:30-12:30</span> <span dir="rtl">א-ה</span><br><span dir="ltr">20:30 - 22:30</span></p>
      <p class="hebrew-address" dir="rtl">מרכז מסחרי גבעת אלון</p>
      <p class="english-address">Givat Alon Shopping Center</p>
      <p class="landmark" dir="rtl">(מעל פלאפל הגן)</p>
      <p class="directions" dir="rtl">ניתן להגיע גם משדרות אלון 16</p>
      <p class="buses">Buses 7, 13, 18, 24, 33, 47, 50, 58, 71, 74, 80</p>
    </div>

    <div class="band-phone">077-5550142</div>
    <div class="band-web">www.orvelle.co.il</div>
  </section>
</div>
</body>
</html>
```